Organic Food company needs a new design label logo

Our company name is Brackwell Dene Organic. We pack organic dried products and sell to natural, organic or small supermarkets in the UK.

We would like to you to design our new label with logo.

The label size should be the width is 65 mm and the length is 85 mm. The label should also include our land stewardship guild and European organic logos.

The food label should reflect our company that we are organic and we sell quality organic food products.

The colours should be pastel and warm colour. It shouldn’t have so many colour.
Updates

Dear All,

Just let you know that this project is food label with the new design. The size of the label should as follow; 
width: 65 mm
length: 85 mm

It will be used for dried fruit, vegetables and nuts. so the middle of the label should be blank, as the print shop will print the name separetly.

When you design our new logo label, please also read my previous note.

Thank you.

Target Market(s)

Above 25 years old. People who like to buy organic or natural food products. Middle income people.

Industry/Entity Type

It Company

Requirements
Must have
• 1) Land Stewardship Guild logo (attached as file )

2) European organic logo ( can be download from http://farmmark-register.example/produce/natural/seal-policy/badge_en )

3) The following information should be either next to or underneath to European logo;
XK-CRT-17
Non-EU Agriculture

The above text information shouldn't be very big.

4) There should be enough space in the middle of the label to write (later by the print shop) full product name and weight.

5) Our company name is "Brackwell Dene Organic"

6) Our web site address is www.brackwelldene.example

```html
<!DOCTYPE html>
<html lang="en">
<head>
<meta charset="utf-8">
<title>Brackwell Dene Organic – Label Designs</title>
<link rel="stylesheet" href="https://fonts.googleapis.com/css2?family=Cinzel:wght@400;600&family=Open+Sans:wght@400;600&display=swap">
<style>
  :root {
    --stage-light: #e4dcc6;
    --stage-dark: #d2c5a6;
    --cream: #fdf3a6;
    --mint: #e7f1d9;
    --orange: #ef6a23;
    --orange-soft: #f6a66a;
    --brown: #6e4526;
    --brown-soft: #b48b68;
    --green: #8cc63f;
    --green-soft: #bcdd8c;
    --grey: #4a4a4a;
    --grey-soft: #9a9a9a;
    --eu-green: #7cc242;
  }
  * { box-sizing: border-box; margin: 0; padding: 0; }
  html, body { width: 1200px; height: 900px; overflow: hidden; }
  body {
    position: relative;
    background: radial-gradient(ellipse at 50% 45%, var(--stage-light) 0%, var(--stage-dark) 100%);
    font-family: "Open Sans", sans-serif;
  }

  /* ---------- label shell ---------- */
  .label {
    position: absolute;
    border-style: solid;
    color: var(--ink);
    background: var(--paper);
  }
  .label--large  { left: 186px; top: 58px;  width: 444px; height: 578px; border-width: 14px;
                   --ink: var(--orange); --soft: var(--orange-soft); --paper: var(--cream); border-color: var(--orange); }
  .label--autumn { left: 728px; top: 58px;  width: 284px; height: 371px; border-width: 8px;
                   --ink: var(--orange); --soft: var(--orange-soft); --paper: var(--mint); --rule: var(--brown); border-color: var(--brown); }
  .label--spring { left: 728px; top: 472px; width: 286px; height: 371px; border-width: 8px;
                   --ink: var(--green); --soft: var(--green-soft); --paper: var(--cream); --rule: var(--brown); border-color: var(--green); }

  .brand-mark {
    position: absolute;
    left: 50%;
    transform: translateX(-50%);
    border-radius: 50%;
    background: var(--soft);
    opacity: .55;
  }
  .brand-name {
    position: absolute;
    left: 0; right: 0;
    text-align: center;
    font-family: "Cinzel", serif;
    font-weight: 600;
    color: var(--ink);
    white-space: nowrap;
  }
  .product-area {
    position: absolute;
    border: 1.5px solid var(--rule, var(--ink));
  }
  .product-area__tag {
    position: absolute;
    left: 50%;
    transform: translate(-50%, -55%);
    top: 0;
    padding: 0 10px;
    background: var(--paper);
    font-family: "Cinzel", serif;
    font-weight: 600;
    color: var(--ink);
    white-space: nowrap;
  }

  .certs {
    position: absolute;
    display: flex;
    align-items: center;
  }
  .certs__seal {
    border-radius: 50%;
    border: 2px solid var(--ink);
    flex: none;
  }
  .certs__eu {
    background: var(--eu-green);
    flex: none;
  }
  .certs__code {
    color: var(--ink);
    line-height: 1.25;
  }

  /* large label sizes */
  .label--large .brand-mark { top: 42px; width: 136px; height: 136px; }
  .label--large .brand-name { top: 196px; font-size: 40px; }
  .label--large .product-area { left: 32px; top: 266px; width: 353px; height: 202px; }
  .label--large .product-area__tag { font-size: 19px; letter-spacing: 5px; }
  .label--large .certs { left: 110px; top: 482px; gap: 12px; }
  .label--large .certs__seal { width: 46px; height: 46px; }
  .label--large .certs__eu { width: 62px; height: 40px; }
  .label--large .certs__code { font-size: 11px; }

  /* small label sizes */
  .label--autumn .brand-mark,
  .label--spring .brand-mark { top: 14px; width: 94px; height: 94px; }
  .label--autumn .brand-name,
  .label--spring .brand-name { top: 122px; font-size: 25px; }
  .label--autumn .product-area,
  .label--spring .product-area { left: 20px; top: 170px; width: 228px; height: 130px; }
  .label--autumn .product-area__tag,
  .label--spring .product-area__tag { font-size: 12px; letter-spacing: 3px; }
  .label--autumn .certs,
  .label--spring .certs { left: 64px; top: 314px; gap: 8px; }
  .label--autumn .certs__seal,
  .label--spring .certs__seal { width: 26px; height: 26px; border-width: 1.5px; }
  .label--autumn .certs__eu,
  .label--spring .certs__eu { width: 36px; height: 24px; }
  .label--autumn .certs__code,
  .label--spring .certs__code { font-size: 7px; }

  /* standalone mono logo */
  .logo-mono {
    position: absolute;
    left: 268px; top: 668px;
    width: 270px; height: 190px;
    --ink: var(--grey);
    --soft: var(--grey-soft);
  }
  .logo-mono .brand-mark { top: 6px; width: 100px; height: 100px; }
  .logo-mono .brand-name { top: 116px; font-size: 28px; }
  .logo-mono__tag {
    position: absolute;
    left: 0; right: 0; top: 162px;
    display: flex;
    align-items: center;
    gap: 10px;
    font-family: "Cinzel", serif;
    font-weight: 600;
    font-size: 15px;
    letter-spacing: 5px;
    color: var(--grey);
  }
  .logo-mono__tag::before,
  .logo-mono__tag::after {
    content: "";
    flex: 1;
    height: 1.5px;
    background: var(--grey);
  }
</style>
</head>
<body>

  <section class="label label--large" aria-label="Large label, orange">
    <div class="brand-mark" aria-hidden="true"></div>
    <div class="brand-name">Brackwell Dene</div>
    <div class="product-area">
      <span class="product-area__tag">ORGANIC</span>
    </div>
    <div class="certs">
      <span class="certs__seal" role="img" aria-label="Land Stewardship Guild certification badge"></span>
      <span class="certs__eu" role="img" aria-label="European organic badge"></span>
      <span class="certs__code">XK-CRT-17<br>Non-EU Agriculture</span>
    </div>
  </section>

  <section class="label label--autumn" aria-label="Small label, brown and orange">
    <div class="brand-mark" aria-hidden="true"></div>
    <div class="brand-name">Brackwell Dene</div>
    <div class="product-area">
      <span class="product-area__tag">ORGANIC</span>
    </div>
    <div class="certs">
      <span class="certs__seal" role="img" aria-label="Land Stewardship Guild certification badge"></span>
      <span class="certs__eu" role="img" aria-label="European organic badge"></span>
      <span class="certs__code">XK-CRT-17<br>Non-EU Agriculture</span>
    </div>
  </section>

  <section class="label label--spring" aria-label="Small label, green">
    <div class="brand-mark" aria-hidden="true"></div>
    <div class="brand-name">Brackwell Dene</div>
    <div class="product-area">
      <span class="product-area__tag">ORGANIC</span>
    </div>
    <div class="certs">
      <span class="certs__seal" role="img" aria-label="Land Stewardship Guild certification badge"></span>
      <span class="certs__eu" role="img" aria-label="European organic badge"></span>
      <span class="certs__code">XK-CRT-17<br>Non-EU Agriculture</span>
    </div>
  </section>

  <section class="logo-mono" aria-label="Single-colour logo">
    <div class="brand-mark" aria-hidden="true"></div>
    <div class="brand-name">Brackwell Dene</div>
    <div class="logo-mono__tag">ORGANIC</div>
  </section>

</body>
</html>
```